Letterhead and envelope design

Using current logo and colours I would like to have a new design done for a stationary set to be printed.

The new files should include logo, web and email address as well as,mailing address and phone number

Dov Harmsby
Harmsby Construction Inc
Box 27 Site 18 RR5
Larkmoor Valley
T4K 2B9
Cell : 403-555-2917
Email: dov@harmsbyconstruction.example
web: harmsbyconstruction.example

```html
<!DOCTYPE html>
<html lang="en">
<head>
<meta charset="utf-8">
<title>Harmsby Construction Letterhead</title>
<link href="https://fonts.googleapis.com/css2?family=Roboto:wght@400;500;700&display=swap" rel="stylesheet">
<style>
  :root {
    --navy: #1d3a6b;
    --orange: #f29a1f;
    --ink: #3a3a3a;
    --frame: #d9d9d9;
    --paper: #ffffff;
  }
  * { box-sizing: border-box; margin: 0; padding: 0; }
  html, body { width: 874px; height: 1200px; overflow: hidden; }
  body {
    background: var(--frame);
    font-family: "Roboto", Arial, sans-serif;
    color: var(--ink);
  }
  .sheet {
    position: absolute;
    left: 10px; top: 10px;
    width: 854px; height: 1180px;
    background: var(--paper);
  }
  .header-rule {
    position: absolute;
    left: 0; right: 0; top: 96px;
    height: 4px;
    background: var(--orange);
  }
  .brand {
    position: absolute;
    left: 50%; top: 58px;
    transform: translateX(-50%);
    display: flex; align-items: center; gap: 14px;
    background: var(--paper);
    padding: 0 18px;
  }
  .brand-dot {
    width: 80px; height: 80px; border-radius: 50%;
    background: var(--navy);
  }
  .brand-name {
    font-weight: 700;
    font-size: 30px;
    line-height: 1.05;
    color: var(--navy);
    letter-spacing: 0.5px;
  }
  .date {
    position: absolute;
    right: 92px; top: 328px;
    font-size: 15px;
  }
  .letter {
    position: absolute;
    left: 92px; right: 92px; top: 402px;
    font-size: 15px;
    line-height: 23px;
  }
  .salutation { margin-bottom: 14px; }
  .letter p.body {
    text-align: justify;
    margin-bottom: 42px;
  }
  .closing { margin-top: 32px; }
  .signature {
    margin-top: 14px;
    width: 150px; height: 44px;
    background: linear-gradient(90deg, #e6e6e6, #f4f4f4);
    border-radius: 4px;
  }
  .footer-rule {
    position: absolute;
    left: 0; right: 0; top: 1058px;
    height: 4px;
    background: var(--orange);
  }
  .contacts {
    position: absolute;
    left: 20px; right: 20px; top: 1036px;
    display: flex; justify-content: space-between;
  }
  .contact {
    width: 25%;
    display: flex; flex-direction: column; align-items: center;
    font-size: 12.5px; font-weight: 500; line-height: 17px;
    text-align: center;
    white-space: nowrap;
  }
  .contact svg { width: 48px; height: 48px; margin-bottom: 12px; }
</style>
</head>
<body>
<div class="sheet">
  <div class="header-rule"></div>
  <div class="brand">
    <span class="brand-dot"></span>
    <span class="brand-name">HARMSBY<br>CONSTRUCTION</span>
  </div>

  <div class="date">XX-XX-XXXX</div>

  <div class="letter">
    <p class="salutation">Dear Clients</p>
    <p class="body">Lorem ipsum dolor sit amet, consectetur adipiscing elit, sed do eiusmod tempor incididunt ut labore et dolore magna aliqua. Ut enim ad minim veniam, quis nostrud exercitation ullamco laboris nisi ut aliquip ex ea commodo consequat. Duis aute irure dolor in reprehenderit in voluptate velit esse cillum dolore eu fugiat nulla pariatur. Excepteur sint occaecat cupidatat non proident, sunt in culpa qui officia deserunt mollit anim id est laborum.</p>
    <p class="body">Lorem ipsum dolor sit amet, consectetur adipiscing elit, sed do eiusmod tempor incididunt ut labore et dolore magna aliqua. Ut enim ad minim veniam, quis nostrud exercitation ullamco laboris nisi ut aliquip ex ea commodo consequat. Duis aute irure dolor in reprehenderit in voluptate velit esse cillum dolore eu fugiat nulla pariatur. Excepteur sint occaecat cupidatat non proident, sunt in culpa qui officia deserunt mollit anim id est laborum.</p>
    <p class="body">Lorem ipsum dolor sit amet, consectetur adipiscing elit, sed do eiusmod tempor incididunt ut labore et dolore magna aliqua. Ut enim ad minim veniam, quis nostrud exercitation ullamco laboris nisi ut aliquip ex ea commodo consequat. Duis aute irure dolor in reprehenderit in voluptate velit esse cillum dolore eu fugiat nulla pariatur. Excepteur sint occaecat cupidatat non proident, sunt in culpa qui officia deserunt mollit anim id est laborum.</p>
    <p class="closing">Sincerly,</p>
    <div class="signature" role="img" aria-label="Handwritten signature"></div>
  </div>

  <div class="footer-rule"></div>
  <div class="contacts">
    <div class="contact">
      <svg viewBox="0 0 48 48" aria-hidden="true"><circle cx="24" cy="24" r="24" fill="var(--navy)"/><path d="M24 12a8 8 0 0 0-8 8c0 6 8 15 8 15s8-9 8-15a8 8 0 0 0-8-8zm0 11a3 3 0 1 1 0-6 3 3 0 0 1 0 6z" fill="#fff"/></svg>
      <span>Box 27 Site 18 RR5<br>Larkmoor Valley T4K 2B9</span>
    </div>
    <div class="contact">
      <svg viewBox="0 0 48 48" aria-hidden="true"><circle cx="24" cy="24" r="24" fill="var(--navy)"/><g fill="none" stroke="#fff" stroke-width="2"><circle cx="24" cy="24" r="11"/><ellipse cx="24" cy="24" rx="5" ry="11"/><path d="M13 24h22M15 18h18M15 30h18"/></g></svg>
      <span>www.harmsbyconstruction.example</span>
    </div>
    <div class="contact">
      <svg viewBox="0 0 48 48" aria-hidden="true"><circle cx="24" cy="24" r="24" fill="var(--navy)"/><path d="M17 13l4 0 2 6-3 2c1 3 4 6 7 7l2-3 6 2v4c0 1-1 2-2 2-10 0-18-8-18-18 0-1 1-2 2-2z" fill="#fff"/></svg>
      <span>403-555-2917</span>
    </div>
    <div class="contact">
      <svg viewBox="0 0 48 48" aria-hidden="true"><circle cx="24" cy="24" r="24" fill="var(--navy)"/><rect x="13" y="16" width="22" height="16" rx="2" fill="#fff"/><path d="M13 17l11 9 11-9" fill="none" stroke="var(--navy)" stroke-width="2"/></svg>
      <span>dov@harmsbyconstruction.example</span>
    </div>
  </div>
</div>
</body>
</html>
```